TalentHive web site

We need a new look for our web site TalentHive-software.example, we use a lot of keywords to maximize our organic searches as well as Searchly landing pages.

Our product TalentHive is a web based Saas applicant & recruiting solution, so with the "cloud" being one of the bid IT buzzes lately we want to leverage that.

We will want to have 3 options for companies a Basic, Professional & Enterprise, with a grid of feature offerings the buyer can choose from.

We also want a strong call to action to enroll in a free webinar.

Target Market(s)

HR and Recruiters for mid to large size employers. No market vertical

Requirements
Must have
• Strong graphics, we currently have some screen shots.

```html
<!DOCTYPE html>
<html lang="en">
<head>
<meta charset="utf-8">
<title>TalentHive – Recruiting &amp; Applicant Tracking Software</title>
<link rel="stylesheet" href="https://fonts.googleapis.com/css2?family=Open+Sans:wght@300;400;600;700&family=Roboto+Condensed:wght@400;700&display=swap">
<style>
:root{
  --brand-blue:#1a7fc1;
  --brand-red:#c0393b;
  --accent-cyan:#3fb4e8;
  --ink:#333;
  --muted:#666;
  --green:#3a9a2a;
  --dark:#1c1c1c;
  --panel:#f4f4f4;
  --line:#d9d9d9;
}
*{box-sizing:border-box;margin:0;padding:0}
html,body{width:883px;height:1200px;overflow:hidden;background:#fff}
body{font-family:"Open Sans",Arial,sans-serif;color:var(--ink)}
.page{position:relative;width:883px;height:1200px;overflow:hidden}
.abs{position:absolute}

/* header */
.logo{left:104px;top:12px;font-size:42px;line-height:52px;font-weight:600;color:var(--brand-blue);letter-spacing:-1px;white-space:nowrap}
.call{right:104px;top:10px;font-size:11.5px;color:var(--brand-red);display:flex;align-items:center;gap:6px;white-space:nowrap}
.call .num{background:var(--dark);color:#fff;border-radius:10px;padding:2px 8px 2px 6px;font-size:11px}
.nav{right:96px;top:43px;display:flex;align-items:center;font-size:12px;white-space:nowrap}
.nav a{color:#333;text-decoration:none;padding:0 11px;line-height:24px;white-space:nowrap}
.nav a.active{background:var(--brand-red);color:#fff;border-radius:2px;padding:0 15px;margin-right:2px}

/* hero */
.hero{left:0;top:79px;width:883px;height:311px;background:linear-gradient(90deg,#1e1e1e 0%,#3a3a3a 35%,#8c8c8c 60%,#d8d8d8 80%,#bdbdbd 100%)}
.hero-photo{left:430px;top:79px;width:453px;height:311px;background:radial-gradient(ellipse at 55% 55%,rgba(70,70,80,.55),rgba(200,200,205,0) 70%)}
.hero-title{left:104px;top:153px;color:#fff;font-size:30px;line-height:36px;font-weight:700;letter-spacing:.5px;white-space:nowrap}
.hero-title small{font-size:17px;font-style:italic;font-weight:400}
.hero-sub{left:104px;top:187px;color:#fff;font-size:16.5px;line-height:22px;font-weight:300;white-space:nowrap}
.benefits{left:108px;top:226px;list-style:none;color:#fff;font-size:12.8px;line-height:15.5px}
.benefits li{padding-left:16px;position:relative;white-space:nowrap}
.benefits li::before{content:"";position:absolute;left:0;top:6px;border-left:4px solid #fff;border-top:2.5px solid transparent;border-bottom:2.5px solid transparent}
.benefits b{color:var(--accent-cyan);font-weight:700}

/* features */
.section-title{left:0;width:883px;top:410px;text-align:center;font-size:16.5px;font-weight:700;color:var(--brand-blue)}
.section-title .red{color:var(--brand-red)}
.rule{left:104px;width:675px;height:1px;background:var(--line)}
.plan{width:200px;text-align:center}
.plan svg{display:block;margin:0 auto}
.plan h3{font-weight:400;font-size:14px;margin-top:6px;color:#222}
.plan.pro h3{color:var(--brand-blue)}
.plan p{font-size:8.3px;color:var(--muted);line-height:12px;margin-top:5px;padding:0 8px}
.plan a{display:block;font-size:9px;color:var(--green);text-decoration:none;margin-top:6px}

/* lower band */
.band{left:0;top:672px;width:883px;height:403px;background:var(--panel);border-top:1px solid #e4e4e4}
.band-title{left:104px;top:711px;font-family:"Roboto Condensed",Arial,sans-serif;font-weight:700;font-size:18px;color:var(--brand-blue);white-space:nowrap}
.band-title .red{color:var(--brand-red)}
.video{left:104px;top:751px;width:442px;height:199px;border:1px solid #c99;overflow:hidden}
.video .scene{position:absolute;inset:0;background:linear-gradient(180deg,#9a9a9a 0%,#c9c9c9 45%,#e3e3e3 70%,#bdbdbd 100%)}
.video .play{position:absolute;left:205px;top:82px;width:38px;height:22px;background:rgba(20,20,20,.85);border-radius:2px}
.video .play::after{content:"";position:absolute;left:16px;top:6px;border-left:9px solid #fff;border-top:5px solid transparent;border-bottom:5px solid transparent}
.video .bar{position:absolute;left:0;bottom:0;width:100%;height:20px;background:#111;color:#ddd;font-size:7.5px;display:flex;align-items:center;padding:0 6px;gap:8px}
.video .track{flex:1;height:6px;background:#555;border-radius:3px;position:relative}
.video .track i{position:absolute;left:0;top:0;height:6px;width:45%;background:#ccc;border-radius:3px}
.intro{left:104px;top:964px;width:452px;font-size:12.6px;font-weight:300;color:#444;line-height:16px}
.more{left:104px;top:1025px;background:var(--dark);color:#fff;font-size:8.5px;padding:4px 8px;border-radius:1px}

/* form */
.demo{left:571px;top:712px;width:209px;height:330px;background:#eef0f2;border:1px solid #cfe0ec}
.demo-head{left:571px;top:712px;width:209px;height:34px;background:var(--brand-blue);color:#fff;font-family:"Roboto Condensed",Arial,sans-serif;font-weight:700;font-size:10.2px;line-height:34px;text-align:center;white-space:nowrap}
.demo-head::after{content:"";position:absolute;left:30px;bottom:-7px;border-top:7px solid var(--brand-blue);border-left:6px solid transparent;border-right:6px solid transparent}
.field{left:584px;width:181px;height:22px;background:#fff;border:1px solid #ccc;font-size:8.6px;color:#555;padding:6px 9px;white-space:nowrap}
.field span,.req span{color:var(--brand-blue)}
.field.select .arrow{position:absolute;right:2px;top:2px;width:17px;height:16px;background:var(--brand-blue)}
.field.select .arrow::after{content:"";position:absolute;left:4px;top:5px;border-top:6px solid #fff;border-left:4.5px solid transparent;border-right:4.5px solid transparent}
.field.area{height:49px}
.req{left:590px;top:1013px;font-size:8.5px;color:#555}
.submit{left:689px;top:1006px;width:77px;height:24px;background:var(--brand-red);color:#fff;font-size:12.5px;text-align:center;line-height:24px}

/* footer */
.foot{left:0;width:883px;text-align:center;font-size:9px;color:#222}
.phone{left:0;width:883px;text-align:center;font-family:"Roboto Condensed",Arial,sans-serif;font-size:19px;color:#111;display:flex;justify-content:center;align-items:center;gap:6px}
</style>
</head>
<body>
<div class="page">

  <header>
    <div class="abs logo">TalentHive</div>
    <div class="abs call">Call Us Now
      <svg width="10" height="16" viewBox="0 0 10 16" aria-hidden="true"><rect x="0.5" y="0.5" width="9" height="15" rx="1.5" fill="#222"/><rect x="2" y="2" width="6" height="9" fill="#fff"/></svg>
      <span class="num">1-800-555-0142</span>
    </div>
    <nav class="abs nav">
      <a class="active" href="#">About TalentHive</a>
      <a href="#">Tour</a>
      <a href="#">Testimonials</a>
      <a href="#">Brochure</a>
      <a href="#">Blog</a>
    </nav>
  </header>

  <section>
    <div class="abs hero"></div>
    <div class="abs hero-photo" role="img" aria-label="Photo of a smiling team of four business professionals"></div>
    <h1 class="abs hero-title">Benefits <small>of</small> TalentHive</h1>
    <div class="abs hero-sub">Recruiting and Applicant Tracking Software</div>
    <ul class="abs benefits">
      <li>Upgrade your <b>current</b> process.</li>
      <li>Say goodbye to emails and PDFs.</li>
      <li>Integrates with your <b>website</b>!</li>
      <li><b>Flexible</b> and customizable job applications.</li>
      <li>Quickly find the most qualified <b>candidates</b> for the job!</li>
      <li>Comprehensive <b>pre-formatted</b> reports.</li>
      <li><b>Social Media</b> Integration.</li>
    </ul>
  </section>

  <section>
    <h2 class="abs section-title"><span class="red">OUR</span> COMPANIES FEATURES</h2>
    <div class="abs rule" style="top:446px"></div>

    <div class="abs plan" style="left:108px;top:472px">
      <svg width="120" height="78" viewBox="0 0 120 78" aria-hidden="true">
        <path d="M20 76 C4 76 0 62 6 54 C12 44 24 44 30 46 C34 22 52 4 76 6 C96 8 104 28 100 44 C114 44 122 56 118 66 C114 74 108 76 100 76 Z" fill="#2a2a2a"/>
        <g fill="none" stroke="#fff" stroke-width="2.2"><rect x="42" y="44" width="10" height="18"/><rect x="55" y="36" width="10" height="26"/><rect x="68" y="26" width="10" height="36"/></g>
      </svg>
      <h3>Basic</h3>
      <p>Lorem Ipsum is simply dummy text of the printing and typesetting industry. Lorem Ipsum has been...</p>
      <a href="#">Learn More</a>
    </div>

    <div class="abs plan pro" style="left:346px;top:472px">
      <svg width="120" height="78" viewBox="0 0 120 78" aria-hidden="true">
        <path d="M20 76 C4 76 0 62 6 54 C12 44 24 44 30 46 C34 22 52 4 76 6 C96 8 104 28 100 44 C114 44 122 56 118 66 C114 74 108 76 100 76 Z" fill="#1470b5"/>
        <circle cx="62" cy="36" r="8" fill="#fff"/><path d="M46 64 C46 50 52 46 62 46 C72 46 78 50 78 64 Z" fill="#fff"/>
      </svg>
      <h3>Professional</h3>
      <p>It is a long established fact that a reader will be distracted by the readable content of a page...</p>
      <a href="#">Learn More</a>
    </div>

    <div class="abs plan" style="left:584px;top:472px">
      <svg width="120" height="78" viewBox="0 0 120 78" aria-hidden="true">
        <path d="M20 76 C4 76 0 62 6 54 C12 44 24 44 30 46 C34 22 52 4 76 6 C96 8 104 28 100 44 C114 44 122 56 118 66 C114 74 108 76 100 76 Z" fill="#2a2a2a"/>
        <rect x="52" y="26" width="22" height="38" fill="#fff"/>
        <g fill="#2a2a2a"><rect x="55" y="29" width="4" height="4"/><rect x="61" y="29" width="4" height="4"/><rect x="67" y="29" width="4" height="4"/><rect x="55" y="36" width="4" height="4"/><rect x="61" y="36" width="4" height="4"/><rect x="67" y="36" width="4" height="4"/><rect x="55" y="43" width="4" height="4"/><rect x="61" y="43" width="4" height="4"/><rect x="67" y="43" width="4" height="4"/><rect x="60" y="53" width="6" height="11"/></g>
      </svg>
      <h3>Enterprise</h3>
      <p>There are many variations of passages of Lorem Ipsum available, but the majority have suffered alteration...</p>
      <a href="#">Learn More</a>
    </div>
  </section>

  <section>
    <div class="abs band"></div>
    <h2 class="abs band-title"><span class="red">TalentHive, Recruiting</span> &amp; Applicant Tracking Software</h2>
    <div class="abs video">
      <div class="scene" role="img" aria-label="Video still of colleagues meeting around a laptop"></div>
      <div class="play"></div>
      <div class="bar"><span>&#9654;</span><span>00:30</span><div class="track"><i></i></div><b>HD</b><span>&#9835;</span></div>
    </div>
    <p class="abs intro">TalentHive is a hosted SaaS (Software as a Service), cloud-based recruiting software designed to provide any size of business a cost effective, affordable and simple way to manage the recruiting process online.</p>
    <div class="abs more">View More &#8250;</div>

    <div class="abs demo"></div>
    <div class="abs demo-head">Register for your FREE TalentHive Demo Today!</div>
    <div class="abs field" style="top:768px">Name<span>*</span></div>
    <div class="abs field" style="top:794px">Company Name<span>*</span></div>
    <div class="abs field" style="top:821px">Phone Number<span>*</span></div>
    <div class="abs field" style="top:847px">E-mail Address<span>*</span></div>
    <div class="abs field" style="top:873px">What HR system are you using<span>*</span></div>
    <div class="abs field" style="top:900px">How were you referred<span>*</span></div>
    <div class="abs field select" style="top:926px">Select Demo Date<span>*</span><div class="arrow"></div></div>
    <div class="abs field area" style="top:952px">Questions or Comments<span>*</span></div>
    <div class="abs req">Required Field<span>*</span></div>
    <div class="abs submit">SUBMIT</div>
  </section>

  <footer>
    <div class="abs foot" style="top:1095px">TalentHive Web-based software is developed and owned by Northpoint Systems 48 Elm Avenue • Brookvale, ST 00000</div>
    <div class="abs foot" style="top:1111px">©2013 TalentHive-software.example All Rights Reserved.</div>
    <div class="abs phone" style="top:1130px">
      <svg width="16" height="17" viewBox="0 0 16 17" aria-hidden="true"><rect x="2" y="4" width="9" height="12" rx="1" fill="none" stroke="#111" stroke-width="1.6"/><rect x="4" y="6" width="5" height="4" fill="#111"/><path d="M10 4 L14 1" stroke="#111" stroke-width="1.6"/></svg>
      800-555-0142</div>
    <div class="abs phone" style="top:1152px">
      <svg width="17" height="16" viewBox="0 0 17 16" aria-hidden="true"><rect x="1" y="4" width="15" height="11" rx="1" fill="none" stroke="#111" stroke-width="1.6"/><rect x="3" y="1" width="4" height="12" fill="#111"/><g fill="#111"><rect x="9" y="7" width="2" height="2"/><rect x="12" y="7" width="2" height="2"/><rect x="9" y="10" width="2" height="2"/><rect x="12" y="10" width="2" height="2"/></g></svg>
      860-555-0178</div>
  </footer>

</div>
</body>
</html>
```